Tidewell Strength Nutrition Booklet

Task Description

**Project Title**: Tidewell Strength Nutrition Introductory Document Design

**Description**:
We need a comprehensive and visually appealing introductory document for Tidewell Strength, a specialized gym based in Victoria, British Columbia. Our gym focuses on personal training, habit changing, and nutrition coaching, with a special emphasis on longevity. This document will be used to introduce new clients to our nutrition programming, providing them with all necessary information, tips, and guidance to support their health and wellness journey.

**Business Background**:
Tidewell Strength is dedicated to helping clients achieve their health and fitness goals through personalized training and nutrition plans. All our coaches hold degrees in sports science and are committed to promoting long-term health and longevity. We offer various services, including screenings, comprehensive testing, nutrition coaching, and assessments of sleep hygiene and stress levels. Our goal is to empower clients to make educated choices for their health and to provide them with the tools they need to succeed.

**Document Requirements**:
1. **Cover Page**:
- Title: "Tidewell Strength Nutrition Introductory Guide"
- Subtitle: "Your Comprehensive Guide to Nutrition and Longevity"
- Include Tidewell Strength logo and branding elements
- Visually engaging design that reflects health, wellness, and longevity

2. **Table of Contents**:
- Organized and easy to navigate sections

3. **Introduction**:
- Brief overview of Tidewell Strength and our nutrition philosophy
- Emphasis on personalized coaching and habit changing

4. **Nutrition Programming Overview**:
- Detailed description of our nutrition coaching services
- Information on how we integrate nutrition with personal training for optimal results
- Explanation of the role of nutrition in longevity and overall health

5. **Meal Prep Tips and Tricks**:
- Practical advice for meal planning and preparation
- Tips for maintaining a balanced and nutritious diet
- Easy-to-follow guidelines and examples

6. **Sample Meal Plans**:
- Examples of balanced meal plans tailored to different fitness goals
- Nutritional breakdown and portion sizes

7. **Holistic Nutrition and Longevity**:
- Overview of the importance of holistic nutrition in promoting longevity
- Key nutrients and foods that support long-term health

8. **Client Testimonials**:
- Real-life success stories from clients who have benefited from our nutrition coaching

9. **Contact Information**:
- How to reach our nutrition coaches for further guidance and support
- Tidewell Strength contact details (phone number: 250-364-7218, email: info@tidewellstrength.biz)

**Design Preferences**:
- Use a clean, modern, and professional design style
- Incorporate our brand colors (please refer to our logo and branding guidelines)
- Use high-quality images that convey health, wellness, and vitality
- Ensure the document is easy to read with clear headings and subheadings

**Final Deliverables**:
- High-resolution PDF of the complete document
- Source files (e.g., Adobe InDesign or Illustrator) for future edits

We are looking for a design that not only informs but also inspires our clients to take control of their nutrition and health. All of the text is already written with the fonts that we are hoping to use. I will upload it below along with an example of one that I really like from one of our competitors Thank you!

Target Market(s)

### Target Market for Tidewell Strength Nutrition Program **Primary Target Market**: 1. **Age Group**: - Adults aged 35-65 years old 2. **Gender**: - Both males and females 3. **Location**: - Residents of Victoria, British Columbia, and surrounding areas 4. **Demographics**: - Middle to upper-middle class income - Professionals and business owners - Parents, especially those looking to improve family health 5. **Psychographics**: - Health-conscious individuals seeking to improve their overall wellness - People interested in longevity and preventive health - Those who value personalized coaching and tailored fitness plans - Individuals motivated by evidence-based health strategies and scientific approaches 6. **Lifestyle**: - Busy professionals who need efficient and effective nutrition solutions - Active individuals who are already engaged in regular physical activity - People who have tried traditional gyms or diet plans without achieving long-term success - Individuals interested in holistic approaches to health, including nutrition, sleep, and stress management **Secondary Target Market**: 1. **Age Group**: - Young adults aged 25-34 years old 2. **Demographics**: - Young professionals and early-career individuals - Health and fitness enthusiasts 3. **Psychographics**: - Individuals seeking to establish healthy habits early in life - People interested in building a foundation for long-term health and wellness - Those who appreciate innovative and science-based approaches to fitness and nutrition 4. **Lifestyle**: - Tech-savvy individuals who use apps and digital tools for health management - People who participate in community events, such as fitness classes, marathons, and health seminars - Individuals looking for a supportive community and personalized guidance to achieve their health goals **Key Motivations and Pain Points**: 1. **Motivations**: - Desire to improve overall health and wellness - Interest in increasing longevity and quality of life - Seeking personalized and effective nutrition and fitness plans - Need for accountability and expert guidance - Aspiration to maintain a healthy weight and improve physical fitness 2. **Pain Points**: - Frustration with generic diet plans that do not yield results - Difficulty finding reliable and personalized nutrition advice - Struggles with maintaining consistency and motivation - Limited time for meal preparation and planning - Concerns about aging and maintaining health as they get older **Marketing Channels**: - Social media platforms (Instagram, Facebook, LinkedIn) to reach health-conscious individuals and professionals - Email marketing to provide valuable content and updates to our existing and potential clients - Community events and seminars to engage with local residents and promote our services - Collaboration with local health and wellness influencers to expand our reach By understanding and addressing the needs and preferences of our target market, Tidewell Strength can effectively tailor our nutrition program to provide maximum value and support to our clients.

Industry/Entity Type

Health and wellness

Font styles to use
Other font styles liked:
• Fonts are in the document I attached

Requirements
Must have
• ### Project Must-Haves for Tidewell Strength Nutrition Introductory Document 1. **Professional Design**: - Clean, modern, and professional design style that aligns with Tidewell Strength branding. - Use of high-quality images that convey health, wellness, and vitality. - Consistent use of brand colors, fonts, and logos as per our branding guidelines. 2. **Comprehensive Content**: - Detailed overview of Tidewell Strength and its nutrition philosophy. - Clear and engaging introduction to the nutrition program. - Practical meal prep tips and tricks tailored to our clients' needs. - Sample meal plans with nutritional breakdown and portion sizes. - Information on holistic nutrition and its role in promoting longevity. 3. **Client-Centric Approach**: - Easy-to-follow guidelines and actionable advice. - Inclusion of client testimonials to build trust and credibility. - Emphasis on personalized coaching and habit-changing strategies. 4. **Clear Structure and Navigation**: - Organized table of contents for easy navigation. - Clear headings, subheadings, and sections to make the document easy to read. - Logical flow of information from introduction to detailed sections. 5. **Contact and Support Information**: - Prominent display of Tidewell Strength contact details (phone number, email, and website). - Information on how clients can reach our nutrition coaches for further guidance and support. 6. **High-Quality Deliverables**: - High-resolution PDF of the complete document. - Source files (e.g., Adobe InDesign or Illustrator) for future edits and updates. 7. **Engaging Visual Elements**: - Use of infographics and visual aids to simplify complex information. - Inclusion of charts or graphs to illustrate key points and data. 8. **Client Accessibility**: - Ensure the document is accessible and easy to understand for clients with varying levels of nutritional knowledge. - Provide links to additional resources or further reading for interested clients. 9. **Call to Action**: - Clear calls to action throughout the document, encouraging clients to reach out for personalized coaching, book consultations, or engage with additional services. 10. **Review and Feedback**: - Opportunity for review and feedback on draft designs to ensure the final product meets our expectations. - Incorporate any necessary revisions based on feedback to achieve the desired outcome. By including these must-haves, we can ensure the Tidewell Strength Nutrition Introductory Document is both informative and visually appealing, providing valuable support to our clients and enhancing their experience with our nutrition program. ### Tidewell Strength Brand Colors #### Primary Colors - **Navy Blue**: `#001F3F` ![#001F3F](https://via.placeholder.com/50/001F3F/FFFFFF?text=+) - **Muted Earthy Blue**: `#3A5F70` ![#3A5F70](https://via.placeholder.com/50/3A5F70/FFFFFF?text=+) #### Secondary Colors - **White**: `#FFFFFF` ![#FFFFFF](https://via.placeholder.com/50/FFFFFF/000000?text=+) - **Gray**: `#A0A0A0` ![#A0A0A0](https://via.placeholder.com/50/A0A0A0/FFFFFF?text=+) #### Accent Color - **Darker Moss Green**: `#556B2F` ![#556B2F](https://via.placeholder.com/50/556B2F/FFFFFF?text=+) These colors should provide a cohesive, earthy, and professional palette that aligns with the West Coast aesthetic and the branding of Tidewell Strength.
Nice to have
• ### Nice-to-Haves for Tidewell Strength Nutrition Introductory Document 1. **Interactive Elements**: - Incorporate clickable links to recipes, additional resources, or external articles for more in-depth information. - Interactive PDFs with embedded videos explaining meal prep techniques or demonstrating exercises. 2. **Personalized Sections**: - Space for clients to fill in their personal goals, dietary preferences, and notes. - Customizable meal plans that clients can adjust according to their preferences and needs. 3. **Digital Integration**: - QR codes linking to online resources, such as instructional videos, recipe blogs, or workout plans. - Integration with our gym’s app or website for easy access to additional content and tools. 4. **Success Stories and Case Studies**: - Detailed case studies of clients who have successfully improved their health through our nutrition program. - Before-and-after photos and stories to inspire and motivate new clients. 5. **Supplement Recommendations**: - Information on recommended supplements to support various health goals. - Guidelines on how to choose quality supplements and incorporate them into their diet. 6. **Seasonal Meal Plans**: - Sample meal plans that change with the seasons, highlighting seasonal produce and recipes. - Tips for adjusting nutrition habits to fit different times of the year. 7. **Printable Resources**: - Printable grocery shopping lists that align with the meal plans provided. - Meal prep schedules and templates that clients can print and use weekly. 8. **Client Community Section**: - Information about joining our client community, including social media groups or forums. - Opportunities for clients to share their own tips, recipes, and experiences. 9. **Additional Wellness Tips**: - Tips on other aspects of wellness, such as stress management techniques, sleep hygiene, and mindfulness practices. - Brief guides on integrating fitness routines with nutrition plans for holistic health improvement. 10. **Exclusive Discounts**: - Coupons or discounts for local health food stores, restaurants, or wellness products. - Special offers for additional services at Tidewell Strength, like personal training sessions or wellness workshops. 11. **Professional Endorsements**: - Endorsements or tips from our in-house nutrition experts or external health professionals. - Quotes or advice from well-known figures in the fitness and nutrition industry. 12. **Sustainability Tips**: - Information on sustainable eating practices and how to reduce food waste. - Tips for choosing environmentally friendly and ethically sourced food options. Including these nice-to-haves can enhance the value and appeal of the Tidewell Strength Nutrition Introductory Document, providing a more engaging and comprehensive resource for our clients.
Should not have
• Given that you are providing all of the content, here is an updated list of project must not haves: ### Project Must Not Haves (With Provided Content) 1. **Overly Technical Layout**: - Avoid complex layouts that make the document difficult to navigate. - Ensure the design supports easy reading and comprehension. 2. **Cluttered Design**: - Avoid overcrowding pages with too many images or design elements. - Maintain a clean and organized layout to enhance readability. 3. **Inconsistent Branding**: - Do not use colors, fonts, or design elements that deviate from Tidewell Strength’s established branding guidelines. - Ensure all visuals align with our brand identity. 4. **Negative or Fear-Based Imagery**: - Avoid using images that convey negative emotions or fear. - Focus on positive, empowering visuals that inspire and encourage. 5. **Low-Quality Images**: - Do not use low-resolution or irrelevant images. - Ensure all visuals are high-quality and contribute meaningfully to the content. 6. **Distracting or Irrelevant Visuals**: - Avoid using images or design elements that distract from the core content. - Ensure all visual elements are relevant and enhance the message. 7. **Inconsistent Image Style**: - Avoid using images with varying styles and tones that don’t harmonize. - Ensure a consistent visual style throughout the document. 8. **Disorganized Structure**: - Do not present information in a haphazard or disjointed manner. - Ensure a logical flow and clear organization of content. 9. **Excessive White Space or Crowded Pages**: - Avoid pages that are either too sparse or too cluttered. - Balance white space and content to maintain visual appeal. 10. **Unprofessional Tone in Visuals**: - Avoid casual or unprofessional imagery. - Maintain a warm, friendly, and professional tone in all visual elements. 11. **Lack of Visual Hierarchy**: - Do not use designs that lack clear visual hierarchy. - Ensure that important information is highlighted and easily identifiable. 12. **Generic Stock Images**: - Avoid overusing generic stock images that do not add value to the content. - Use images that are specific and relevant to the content provided. This refined list ensures that the visual design complements the provided content effectively, enhancing readability and maintaining professional standards for the Tidewell Strength Nutrition Introductory Document.

```html
<!DOCTYPE html>
<html lang="en">
<head>
<meta charset="utf-8">
<title>Tidewell Strength — Nutrition Introductory Guide</title>
<link rel="stylesheet" href="https://fonts.googleapis.com/css2?family=Montserrat:ital,wght@1,700;1,800;1,900&display=swap">
<style>
  :root {
    --backdrop: #cdcdcd;
    --paper: #ffffff;
    --sky: #a6dff3;
    --citrus: #f9b042;
    --ink: #0a0a0a;
    --photo-light: #ffffff;
    --photo-shade: #e4e1dc;
  }
  * { margin: 0; padding: 0; box-sizing: border-box; }
  html, body {
    width: 1200px;
    height: 2318px;
    overflow: hidden;
    background: var(--backdrop);
    font-family: "Montserrat", Arial, sans-serif;
    font-style: italic;
    color: var(--ink);
  }
  .page {
    position: absolute;
    left: 234px;
    width: 732px;
    height: 1034px;
    background: var(--paper);
    overflow: hidden;
    box-shadow: 4px 5px 6px rgba(0,0,0,0.22);
  }
  .cover { top: 82px; }
  .contents { top: 1200px; }
  .shape { position: absolute; left: 0; top: 0; }

  /* Cover */
  .brand-mark {
    position: absolute;
    left: 84px;
    top: 150px;
    display: flex;
    align-items: center;
    gap: 10px;
    color: var(--paper);
    font-weight: 800;
    font-size: 21px;
    letter-spacing: 0.5px;
  }
  .brand-mark .dot {
    width: 18px; height: 18px;
    border-radius: 50%;
    background: var(--paper);
    flex: none;
  }
  .brand-mark .name { line-height: 1.15; width: 120px; }
  .cover-photo {
    position: absolute;
    left: 0; top: 580px;
    width: 732px; height: 454px;
    background: linear-gradient(180deg, var(--photo-light) 0%, #f6f5f3 45%, var(--photo-shade) 100%);
  }
  .title {
    position: absolute;
    left: 73px;
    top: 368px;
    font-weight: 900;
    line-height: 1;
    white-space: nowrap;
  }
  .title .line-one { display: block; font-size: 62px; letter-spacing: -1.5px; }
  .title .line-two { display: block; font-size: 96px; margin-top: 10px; letter-spacing: -3px; }
  .guide-name {
    position: absolute;
    left: 73px;
    top: 582px;
    font-weight: 900;
    font-size: 31px;
    letter-spacing: -0.8px;
    text-transform: uppercase;
    white-space: nowrap;
  }
  .tagline {
    position: absolute;
    left: 73px;
    top: 664px;
    font-weight: 800;
    font-size: 22px;
    line-height: 31px;
    letter-spacing: -0.3px;
  }

  /* Contents */
  .contents-title {
    position: absolute;
    left: 116px;
    top: 170px;
    font-weight: 900;
    font-size: 62px;
    line-height: 74px;
    letter-spacing: -1px;
  }
  .toc {
    position: absolute;
    left: 116px;
    top: 462px;
    list-style: none;
  }
  .toc li {
    display: flex;
    height: 48px;
    align-items: center;
    font-weight: 800;
    font-size: 22px;
    letter-spacing: -0.2px;
  }
  .toc .num { width: 88px; }
</style>
</head>
<body>

<section class="page cover">
  <svg class="shape" width="732" height="1034" viewBox="0 0 732 1034" aria-hidden="true">
    <path d="M0 0 H210 L385 180 L305 262 C250 312 180 322 120 310 C70 298 30 278 0 250 Z" fill="var(--sky)"/>
  </svg>
  <div class="brand-mark">
    <span class="dot"></span>
    <span class="name">Tidewell Strength</span>
  </div>

  <div class="cover-photo" role="img" aria-label="Photo of a yellow bowl filled with fresh fruit, cucumber and greens beside a stethoscope and capsules on a light table"></div>
  <svg class="shape" width="732" height="1034" viewBox="0 0 732 1034" aria-hidden="true">
    <polygon points="451,749 732,1020 732,1034 248,1034" fill="var(--citrus)" opacity="0.85"/>
  </svg>

  <h1 class="title">
    <span class="line-one">TIDEWELL</span>
    <span class="line-two">STRENGTH</span>
  </h1>
  <p class="guide-name">Nutrition Introductory Guide</p>
  <p class="tagline">Your Comprehensive Guide<br>to Nutrition and Longevity</p>
</section>

<section class="page contents">
  <svg class="shape" width="732" height="1034" viewBox="0 0 732 1034" aria-hidden="true">
    <path d="M289 0 H732 V258 C660 264 600 248 545 198 Z" fill="var(--sky)"/>
    <path d="M0 525 C90 420 200 362 316 362 C420 362 500 400 560 455 L732 619 V937 L629 1034 H154 L0 875 Z" fill="var(--citrus)"/>
  </svg>

  <h2 class="contents-title">Table<br>Of Contents</h2>

  <ol class="toc">
    <li><span class="num">01</span><span>Our Beliefs</span></li>
    <li><span class="num">02</span><span>What to Expect from Us</span></li>
    <li><span class="num">03</span><span>Nutritional Guidelines</span></li>
    <li><span class="num">04</span><span>Added Benefits</span></li>
    <li><span class="num">05</span><span>Meet Our Team</span></li>
    <li><span class="num">06</span><span>Wholesome Recipes</span></li>
    <li><span class="num">07</span><span>Fitness Tracking Advice</span></li>
    <li><span class="num">08</span><span>Your Commitment to Success</span></li>
    <li><span class="num">09</span><span>Contact Details</span></li>
    <li><span class="num">10</span><span>Pathway to Success</span></li>
  </ol>
</section>

</body>
</html>
```